Flyer for an pediatric sleep consultancy - to distribute to play and childcare centers etc.

I need a flyer that will attract the attention of parents with children between the age of babies to toddlers, who may be experiencing sleep issues. The flyer will be placed at places such as community centers, doctors room, play centers, kindergardens, etc.

My company is called "The Quiet Meadow Nest" and provides a sleep consultancy service. My service essentially provides a customized plan for parents to follow and general advice and guidance. It is not medical advice.

I like to the flyer to have an overall tone that is soft and peaceful with a clean and beautiful design, however can catch the attention of parents who may be struggling with their child's sleep issues and are sleep deprived. I would like photos with minimal text. The colour I use is a brownish rose. I will attach some of my designs to give you an idea. You can have a look at my homepage as well to get an idea about my esthetic direction and the colour. Although the colour of my page is a bit too brownish....

I will provide the text to appear in the flyer once I have a better idea of the layout that I prefer for the flyer. The text however wont be extensive, just some catchy points.

I want to direct people to my website which is www.thequietmeadownest.example
I offer a first FREE evaluation call, to the parents, to get to know each other better, learn about their child's particular sleep problems and see if we are a good fit and can work together. I would like to have this information somehow on the flyer, so that the parents will contact me.
I also have a facebook page, which is: The Quiet Meadow Nest

I have a logo that I would like to appear on the flyer. I will attach the file once the uploader on pixel fair is fixed.

When I print the flyer - I like to print A5 SIZE ... please make sure the formatting is OK for this size.

Here are some text ideas. of course all of it would be too much, I guess. On the front of the flyer I would like to have some catchy phrase or something similar to get people interested and to want to know more. On the back there could be a bit more text and information. But I'm open too suggestions....
I'm not too sure about the wording yet. But here are some text that I might be use:

Is sleep an issue in your home?

Is your baby having trouble sleeping? ... are you?!
I can help!

Sleep, baby, sleep….

Teaching children how to sleep

The Quiet Meadow Nest is a pediatric sleep consultancy that specializes in helping parents with children who struggle to develop good and healthy sleep habits.
Disruptive sleep patterns or not enough sleep can affect the physical, mental and emotional development of your child.

Of course nobody plans to have a sleep problem, but habits can become easily ingrained and spiral quickly out of control and you can find yourself sleep deprived, desperate and not too sure what to do. You see all the other sleeping babies and wish there was someone who understood what you were going through?! Well, there is!

Contact me for a free 15 minute consultation.

This 15 minute „mini“ consultation is a chance to discuss your unique sleep challenges and sleep goals with me. I will provide you with an overview of how I will work with your family to achieve your wildest sleep dreams (goals).
Furthermore do I understand and believe that every child and their family is unique and there is no one size fits all!
I would love to have a chat with you and talk about how I can help make things easier for you and your family!

Do I need a sleep consultant for my child?
The answer is yes if:
- if your child will only fall asleep when nursing or bottle feeding
- if your child needs a dummy or other external aid, like being rocked, patted or taken for a care ride to fall asleep
- if your good night routine is a challenging and exhausting procedure instead of a relaxed and enjoyable moment for the whole family
- if sleep is a constant battle in your home which leaves you feeling frustrated and exhausted
- if your own lack of sleep is taking a toll on you and the whole family

What can I do for you?

I will:

- Guide you to set an age appropriate foundation for good sleep
- Create an individual sleep plan tailored especially to your child’s sleep needs and circumstances
- Help you to teach your childto go to sleep and get back to sleep independently during the night
- show you how to teach your child to take healthful, restorative naps
-Learn

Contact:

Marta Lindqvist
info@thequietmeadownest.example
www.thequietmeadownest.example
+34 612 384 570

Consultations in English, German or Spanish via Phone/Linkly or home consultation

Reason: I have to go on a business trip and won't be able to choose a design until the deadline. During the trip I won't have time to give feedback and ask for changes. thank you

Target Market(s)

parents, sleep deprived mothers, young families, child care provider,

Industry/Entity Type

Baby Care

Contact Information for Business Card

Marta Lindqvist
pediatric sleep consultant
+34 612 384 570

```html
<!DOCTYPE html>
<html lang="en">
<head>
<meta charset="utf-8">
<title>The Quiet Meadow Nest – A5 Flyer</title>
<link rel="stylesheet" href="https://fonts.googleapis.com/css2?family=Montserrat:wght@300;400;600;700&display=swap">
<style>
  :root {
    --backdrop: #575556;
    --teal: #45bccc;
    --teal-soft: #9fdbe3;
    --ink: #6f7f84;
    --ink-strong: #5d6d72;
    --heading: #6a7a7f;
    --contact-name: #3f7f88;
    --white: #ffffff;
    --photo-warm: #f3e6df;
  }
  * { box-sizing: border-box; margin: 0; padding: 0; }
  html, body { width: 1200px; height: 1200px; overflow: hidden; }
  body {
    background: var(--backdrop);
    font-family: "Montserrat", sans-serif;
    color: var(--ink);
    position: relative;
  }
  .page {
    position: absolute;
    top: 220px;
    width: 537px;
    height: 760px;
    overflow: hidden;
  }
  /* Front */
  .front {
    left: 48px;
    background: linear-gradient(180deg, var(--teal) 0%, var(--teal-soft) 35%, #e6f5f7 62%, var(--white) 72%);
  }
  .front-headline {
    position: absolute;
    top: 104px;
    left: 0; right: 0;
    text-align: center;
    font-weight: 300;
    font-size: 40px;
    line-height: 39px;
    color: var(--heading);
    letter-spacing: 0.5px;
  }
  .brand-name {
    position: absolute;
    top: 336px;
    left: 0; right: 0;
    text-align: center;
    font-weight: 300;
    font-size: 31px;
    color: var(--heading);
    letter-spacing: -0.5px;
  }
  .brand-mark {
    position: absolute;
    top: 300px;
    left: 258px;
    width: 20px; height: 20px;
    border-radius: 50%;
    border: 1.5px solid #d99a8c;
  }
  .front-photo {
    position: absolute;
    left: 0; right: 0; bottom: 0;
    height: 320px;
    background:
      radial-gradient(ellipse at 60% 55%, #f6dccd 0%, rgba(246,220,205,0) 55%),
      linear-gradient(180deg, rgba(255,255,255,0) 0%, var(--photo-warm) 40%, var(--white) 100%);
  }
  /* Back */
  .back {
    left: 615px;
    background: linear-gradient(180deg, var(--white) 0%, #f4f8f8 50%, #bfe7ec 64%, #7fd0da 80%, var(--teal) 100%);
  }
  .back-photo {
    position: absolute;
    left: 0; right: 0; top: 0;
    height: 360px;
    background:
      radial-gradient(ellipse at 40% 60%, rgba(240,200,185,0.55) 0%, rgba(240,200,185,0) 50%),
      radial-gradient(ellipse at 85% 25%, rgba(245,215,200,0.5) 0%, rgba(245,215,200,0) 45%);
  }
  .back-content {
    position: absolute;
    left: 37px;
    width: 464px;
    font-size: 11.4px;
    line-height: 13.9px;
    font-weight: 300;
  }
  .intro { top: 40px; }
  .intro p + p { margin-top: 13.9px; }
  .intro strong { font-weight: 600; color: var(--ink-strong); }
  .offer-title {
    position: absolute;
    top: 202px; left: 0; right: 0;
    text-align: center;
    font-weight: 700;
    font-size: 16px;
    color: var(--heading);
  }
  .offer { top: 238px; }
  .column {
    position: absolute;
    top: 350px;
    width: 225px;
    font-size: 11.4px;
    line-height: 13.9px;
    font-weight: 300;
  }
  .column.need { left: 37px; }
  .column.help { left: 277px; width: 220px; }
  .column h2 {
    font-size: 14.5px;
    line-height: 18.5px;
    font-weight: 700;
    color: var(--heading);
    height: 48px;
  }
  .column .lead { margin-bottom: 15px; }
  .column ul { list-style: none; }
  .column li { position: relative; padding-left: 23px; }
  .column li::before { content: "•"; position: absolute; left: 0; }
  .contact {
    position: absolute;
    right: 37px;
    top: 649px;
    text-align: right;
    font-size: 13px;
    line-height: 19.2px;
    font-weight: 300;
    color: var(--white);
  }
  .contact .name { font-weight: 600; color: var(--contact-name); }
  .languages {
    position: absolute;
    right: 37px;
    top: 751px;
    font-size: 8px;
    color: var(--contact-name);
    margin-top: -8px;
  }
</style>
</head>
<body>
  <section class="page front">
    <h1 class="front-headline">Is sleep an issue<br>in your home?</h1>
    <span class="brand-mark" aria-hidden="true"></span>
    <div class="brand-name">The Quiet Meadow Nest</div>
    <div class="front-photo" role="img" aria-label="Photo of a baby sleeping peacefully on white bedding, hugging a soft white toy"></div>
  </section>

  <section class="page back">
    <div class="back-photo" role="img" aria-label="Faded photo of a parent's hand gently holding a baby's hand"></div>

    <div class="back-content intro">
      <p><strong>The Quiet Meadow Nest</strong> is a pediatric sleep consultancy that specializes in helping parents with children who struggle to develop good and healthy sleep habits.<br>Disruptive sleep patterns or not enough sleep can affect the physical, mental and emotional development of your child.</p>
      <p>Of course nobody plans to have a sleep problem, but habits can become easily ingrained and spiral quickly out of control and you can find yourself sleep deprived, desperate and not too sure what to do. You see all the other sleeping babies and wish there was someone who understood what you were going through?! Well, there is!</p>
    </div>

    <h2 class="offer-title">Contact me for a free 15 minute consultation</h2>

    <div class="back-content offer">
      <p>This 15 minute “mini” consultation is a chance to discuss your unique sleep challenges and sleep goals with me. I will provide you with an overview of how I will work with your family to achieve your wildest sleep dreams (goals).<br>Furthermore do I understand and believe that every child and their family is unique and there is no one size fits all!<br>I would love to have a chat with you and talk about how I can help make things easier for you and your family!</p>
    </div>

    <div class="column need">
      <h2>Do I need a sleep<br>consultant for my child?</h2>
      <p class="lead">The answer is yes if:</p>
      <ul>
        <li>If your child will only fall asleep when nursing or bottle feeding;</li>
        <li>If your child needs a dummy or other external aid, like being rocked, patted or taken for a care ride to fall asleep;</li>
        <li>If your good night routine is a challenging and exhausting procedure instead of a relaxed and enjoyable moment for the whole family;</li>
        <li>If sleep is a constant battle in your home which leaves you feeling frustrated and exhausted;</li>
        <li>If your own lack of sleep is taking a toll on you and the whole family.</li>
      </ul>
    </div>

    <div class="column help">
      <h2>What can I do for you?</h2>
      <p class="lead">I will:</p>
      <ul>
        <li>Guide you to set an age appropriate foundation for good sleep;</li>
        <li>Create an individual sleep plan tailored especially to your child’s sleep needs and circumstances;</li>
        <li>Help you to teach your childto go to sleep and get back to sleep independently during the night;</li>
        <li>Show you how to teach your child to take healthful, restorative naps;</li>
        <li>Learn;</li>
      </ul>
    </div>

    <address class="contact" style="font-style:normal">
      <div class="name">Marta Lindqvist</div>
      <div>+34 612 384 570</div>
      <div>info@thequietmeadownest.example</div>
      <div>www.thequietmeadownest.example</div>
    </address>
    <p class="languages">Consultations in English, German or Spanish via Phone/Linkly or home consultation.</p>
  </section>
</body>
</html>
```